Landscaping Contract with customizable fillable form

Need a PDF Template with a format that can be filled in with info by us. Then sent to the customer for signature. form need to be able to be changed for each customer

Industry/Entity Type

Landscaping

Colors
00AB8E
00BBA5
67D7C9
C6EFE9
E9F9F6

```html
<!DOCTYPE html>
<html lang="en">
<head>
<meta charset="UTF-8">
<title>Yard Work Contract</title>
<link href="https://fonts.googleapis.com/css2?family=Lato:wght@400;700&family=Montserrat:wght@800&display=swap" rel="stylesheet">
<style>
  :root {
    --backdrop: #4a4a4a;
    --teal: #00ab8e;
    --teal-bright: #00bba5;
    --paper: #ffffff;
    --ink: #1a1a1a;
    --dots: #222222;
  }
  * { box-sizing: border-box; margin: 0; padding: 0; }
  html, body {
    width: 1200px; height: 1200px; overflow: hidden;
    background: var(--backdrop);
  }
  .contract {
    position: absolute; left: 202px; top: 93px;
    width: 790px; height: 1017px;
    background: var(--paper);
    font-family: 'Lato', sans-serif; color: var(--ink);
  }
  .contract-header {
    position: absolute; left: 0; top: 0; width: 100%; height: 92px;
    background: var(--teal);
    display: flex; align-items: center; justify-content: center;
  }
  .contract-title {
    font-family: 'Montserrat', sans-serif; font-weight: 800;
    font-size: 43px; color: var(--paper); letter-spacing: 0.5px;
  }
  .line {
    position: absolute; font-size: 15px; line-height: 18px; white-space: nowrap;
  }
  .fill {
    display: inline-block; border-bottom: 1.5px dotted var(--dots);
    height: 12px; vertical-align: baseline;
  }
  .agree-heading { font-size: 17.5px; }
  .term {
    position: absolute; left: 51px; width: 730px;
    font-size: 15px; line-height: 18px;
  }
  .term-number {
    position: absolute; left: -28px; top: -1px;
    width: 21px; height: 21px; border-radius: 50%;
    background: var(--teal); color: var(--paper);
    font-size: 12.5px; line-height: 21px; text-align: center;
  }
  .signature-line {
    position: absolute; left: 51px; width: 253px;
    border-bottom: 1.5px dotted var(--dots);
  }
  .signature-label {
    position: absolute; left: 50px; font-size: 17.5px; line-height: 22px;
  }
  .footer-rule {
    position: absolute; left: 0; top: 955px; width: 100%; height: 3px;
    background: var(--teal-bright);
  }
  .footer-band {
    position: absolute; left: 0; top: 965px; width: 100%; height: 52px;
    background: var(--teal);
  }
</style>
</head>
<body>
<main class="contract">
  <header class="contract-header">
    <h1 class="contract-title">YARD WORK CONTRACT</h1>
  </header>

  <p class="line" style="left:22px; top:107px;">This contract is made between <span class="fill" style="width:300px; margin:0 4px;"></span> (hereafter known as the Client) and</p>
  <p class="line" style="left:22px; top:137px;"><span class="fill" style="width:277px;"></span>(hereafter known as the Contractor). The Client desires to have certain</p>
  <p class="line" style="left:22px; top:167px;">maintenance services, described below, performed upon a yard located at <span class="fill" style="width:260px; margin-left:2px;"></span></p>
  <p class="line agree-heading" style="left:22px; top:195px;">Therefore, the parties hereby agree as follows :</p>

  <ol class="terms">
    <li class="term" style="top:230px;"><span class="term-number">1.</span>Client shall grant Contractor access to the yard and its surroundings during regular business hours and other<br>mutually agreeable times.</li>
    <li class="term" style="top:278px;"><span class="term-number">2.</span>(Client or Contractor) shall provide all equipment and consumable supplies necessary to perform maintenance<br>&nbsp;services on the yard.</li>
    <li class="term" style="top:326px; line-height:16px;"><span class="term-number">3.</span>Client shall pay Contractor $X on the first day of each (week or month) for regular maintenance services to be<br>performed during the rest of that (week or month). See "Regular Maintenance" description below.</li>
    <li class="term" style="top:372px;"><span class="term-number">4.</span>Client shall pay Contractor for any additional maintenance or repair work that may become necessary to<br>maintain a pleasing, safe, and horticulturally healthy yard (hereafter known as "ad hoc work"). Contractor<br>shall bill Client for the cost of ad hoc work and Client shall include payment with Client's next payment for<br>regular maintenance.</li>
    <li class="term" style="top:455px;"><span class="term-number">5.</span>Ad hoc work whose cost is less than $50 may be performed by Contractor without Clients explicit<br>authorization. Work which Contractor estimates will cost <b>$50</b> or more shall be authorized by Client before it<br>is performed.</li>
    <li class="term" style="top:522px;"><span class="term-number">6.</span>"Regular Maintenance" shall include removal of debris from the yard; mowing of lawn and trimming of shrubs,<br>trees, and other plants; fertilization and other conditioning of the yard's soil; inspection of plants and soil for<br>pests, and extermination of any pests discovered.</li>
    <li class="term" style="top:588px;"><span class="term-number">7.</span>Contractor shall begin performing regular maintenance on <b>MMODNYYY</b>. Thereafter, regular maintenance<br>shall be performed on a schedule to which the parties agree.</li>
    <li class="term" style="top:637px;"><span class="term-number">8.</span>Either party may terminate this agreement with written notice to the other party. Any payment for services<br>rendered owed by Client shall be due and payable at the time this agreement is terminated.</li>
  </ol>

  <p class="line" style="left:32px; top:687px;">In witness to their agreement to these terms, the Client and Contractor affix their signatures below .</p>

  <section class="signatures">
    <div class="signature-line" style="top:748px;"></div>
    <p class="signature-label" style="top:759px;">Client's Signature, Date</p>
    <div class="signature-line" style="top:822px;"></div>
    <p class="signature-label" style="top:834px;">Contractor's Signature, Date</p>
    <div class="signature-line" style="top:900px;"></div>
    <p class="signature-label" style="top:910px;">Client's printed Name</p>
  </section>

  <div class="footer-rule"></div>
  <footer class="footer-band"></footer>
</main>
</body>
</html>
```